i need a business card design for my family investment company "zentaryo investments" based in dubai. its a diverse investment firm focusing on education, hospitality and automotive. the design has to be modern and try to incorporate the logo "E" in the design. details on card as follow

Yousef R Bin Hadrami
Managing Director
yousef@zentaryo.ae
www.zentaryo.ae

Harbor zone,falcon tower, office 3817, dubai
tel. 04 7391852
mobile.050 8142903

Target Market(s)

card used for networking events and investor meetings

Industry/Entity Type

Hospitality

```html
<!DOCTYPE html>
<html lang="en">
<head>
<meta charset="utf-8">
<title>Zentaryo Investments – Business Card</title>
<link href="https://fonts.googleapis.com/css2?family=Lato:wght@300;400;700&display=swap" rel="stylesheet">
<style>
  :root {
    --page-bg: #e4e5e7;
    --card-bg: #ffffff;
    --ink: #111111;
    --brand-blue: #4a7099;
    --shadow: rgba(0, 0, 0, 0.18);
  }
  * { box-sizing: border-box; margin: 0; padding: 0; }
  html, body {
    width: 1200px;
    height: 926px;
    overflow: hidden;
    background: var(--page-bg);
    font-family: "Lato", sans-serif;
  }
  .sheet {
    width: 1200px;
    height: 926px;
    display: flex;
    flex-direction: column;
    align-items: center;
    justify-content: center;
    gap: 32px;
  }
  .card {
    position: relative;
    width: 740px;
    height: 420px;
    background: var(--card-bg);
    box-shadow: 0 6px 20px var(--shadow);
    overflow: hidden;
  }

  /* Front */
  .card-front {
    display: flex;
    align-items: center;
    justify-content: center;
  }
  .brand-name {
    font-family: "Lato", sans-serif;
    font-weight: 300;
    color: var(--ink);
    text-transform: uppercase;
    white-space: nowrap;
  }
  .card-front .brand-name {
    font-size: 42px;
    letter-spacing: 10px;
  }

  /* Back */
  .card-back .brand-name {
    position: absolute;
    left: 42px;
    top: 40px;
    font-size: 24px;
    letter-spacing: 6px;
  }
  .holder {
    position: absolute;
    left: 42px;
    top: 222px;
  }
  .holder-name {
    font-size: 27px;
    font-weight: 400;
    color: var(--brand-blue);
    line-height: 1.15;
  }
  .holder-title {
    font-size: 14px;
    font-weight: 400;
    color: var(--ink);
    letter-spacing: 0.5px;
    text-transform: uppercase;
    margin-top: 3px;
  }
  .contact {
    position: absolute;
    right: 40px;
    top: 150px;
    text-align: right;
    font-size: 18px;
    line-height: 1.3;
    color: var(--ink);
  }
  .contact-label { color: var(--brand-blue); }
  .divider {
    display: block;
    width: 38px;
    height: 2px;
    background: var(--brand-blue);
    margin: 12px 0 10px auto;
  }
  .address {
    font-size: 18px;
    line-height: 1.3;
    font-weight: 400;
  }
  .footer-bands {
    position: absolute;
    left: 0;
    bottom: 0;
    width: 740px;
    height: 110px;
  }
</style>
</head>
<body>
  <main class="sheet">
    <section class="card card-front" aria-label="Card front">
      <span class="brand-name">Zentaryo Investments</span>
    </section>

    <section class="card card-back" aria-label="Card back">
      <span class="brand-name">Zentaryo Investments</span>

      <div class="holder">
        <p class="holder-name">Yousef R Bin Hadrami</p>
        <p class="holder-title">Managing Director</p>
      </div>

      <div class="contact">
        <p><span class="contact-label">tel.</span> 04 7391852</p>
        <p><span class="contact-label">mobile.</span> 050 8142903</p>
        <p><span class="contact-label">website.</span> www.zentaryo.ae</p>
        <p><span class="contact-label">email.</span> yousef@zentaryo.ae</p>
        <span class="divider"></span>
        <p class="address">Harbor zone,falcon tower,<br>office 3817, dubai</p>
      </div>

      <svg class="footer-bands" viewBox="0 0 740 110" aria-hidden="true">
        <polygon points="0,12 330,26 330,33 0,19" fill="var(--ink)"/>
        <polygon points="0,28 300,40 314,72 0,60" fill="var(--brand-blue)"/>
        <polygon points="322,36 740,54 740,110 346,110" fill="var(--ink)"/>
      </svg>
    </section>
  </main>
</body>
</html>
```